Bastion Electronic Security Web Site

We need a web site for our new company based in Sydney Australia.
We specialize in consulting supplying and installing electronic security systems. These include CCTV, Access control, Alarms, Intercom and Network cabling.
We pride our selves in giving our customers peace of mind giving back security and freedom to our customers. We pride in customer service quality products and expertise with and we do the job as though it is for our personal friends and family.
We need to be able to edit web site contents and update information.
Industry/Entity Type
Electronic

```html
<!DOCTYPE html>
<html lang="en">
<head>
<meta charset="utf-8">
<title>Bastion Electronic Security</title>
<link href="https://fonts.googleapis.com/css2?family=Lato:ital,wght@0,300;0,400;0,700;1,300&display=swap" rel="stylesheet">
<style>
:root{
  --navy:#14284f;
  --bar:#27335a;
  --orange:#e0691d;
  --ink:#333;
  --muted:#555;
  --light:#f3f3f5;
  --footer:#232323;
  --white:#fff;
}
*{box-sizing:border-box;margin:0;padding:0}
html,body{width:834px;height:1200px;overflow:hidden}
body{position:relative;font-family:'Lato',sans-serif;color:var(--ink);background:var(--white)}
.abs{position:absolute}
/* top bar */
.topbar{left:0;top:0;width:834px;height:17px;background:var(--bar);color:var(--white);font-size:7px}
.topbar .contact{left:92px;top:4px;display:flex;gap:10px;align-items:center}
.topbar .sq{display:inline-block;width:6px;height:6px;background:var(--white);margin-right:4px;vertical-align:middle}
.topbar .social{right:92px;top:5px;display:flex;gap:6px}
.dot{width:6px;height:6px;border-radius:50%;background:var(--white)}
/* header */
.brand{left:90px;top:33px;display:flex;align-items:center;gap:8px}
.brand-mark{width:30px;height:30px;background:var(--navy)}
.brand-name{font-size:19px;font-weight:700;color:var(--navy);line-height:1}
.nav{left:334px;top:52px;display:flex;gap:20px;font-size:10px;font-weight:700;color:var(--navy)}
/* hero */
.hero{left:0;top:89px;width:834px;height:293px;background:var(--orange)}
.slide{left:86px;top:25px;width:661px;height:238px;background:var(--white);box-shadow:0 12px 14px -8px rgba(0,0,0,.35)}
.slide-art{left:50px;top:30px;width:570px;height:170px;background:linear-gradient(90deg,#d9d9dc 0%,#bfc2c6 35%,#ffffff 38%,#2a2d32 50%,#4e6272 75%,#cfd1d4 100%);border-radius:6px}
.caption{left:0;bottom:0;width:661px;height:33px;background:#161616;color:var(--white);font-style:italic;font-weight:300;font-size:15px;letter-spacing:1.2px;text-align:center;line-height:33px}
.arrow{top:135px}
/* features */
.service{top:394px;width:110px;text-align:center}
.service .icon{margin:0 auto;width:52px;height:52px;background:var(--navy);position:relative}
.service .icon:after{content:"";position:absolute;left:19px;bottom:-7px;border:7px solid transparent;border-bottom:0;border-top-color:var(--navy)}
.service h3{font-size:9px;font-weight:700;margin-top:12px;height:24px;display:flex;align-items:center;justify-content:center;line-height:1.2}
.service p{font-size:6.5px;line-height:1.6;color:var(--muted);margin-top:5px}
.about{left:550px;top:398px;width:193px;font-size:7.5px;line-height:1.75;color:var(--muted);text-align:justify}
.about p+p{margin-top:12px}
/* band */
.band{left:0;top:548px;width:834px;height:73px;background:var(--navy);color:var(--white)}
.band q{position:absolute;left:87px;top:8px;width:670px;font-size:11px;line-height:1.8;quotes:"“ " " “"}
.btn{background:var(--orange);color:var(--white);text-align:center}
.band .btn{left:616px;top:36px;width:124px;height:26px;line-height:26px;font-size:10px}
/* pride */
.pride{left:0;top:621px;width:834px;height:261px;background:var(--light)}
.pride-photo{left:84px;top:20px;width:214px;height:202px;background:radial-gradient(circle at 45% 60%,#3a3c42 0%,#6f7176 45%,#c6c7ca 80%)}
.pager{left:168px;top:236px;display:flex;gap:6px}
.pager span{width:5px;height:5px;border-radius:50%;background:var(--navy)}
.pager span:first-child{background:var(--orange)}
.intro{left:321px;top:19px;width:420px;font-size:9px;line-height:1.75;color:var(--muted)}
.point{width:200px}
.point svg{position:absolute;left:-34px;top:0}
.point h4{font-size:9.5px;font-weight:700;color:#444}
.point p{font-size:7.2px;line-height:1.8;color:var(--muted);margin-top:3px}
/* ready */
.ready h2{left:94px;top:924px;font-size:12px;font-weight:400}
.ready p{left:94px;top:958px;width:312px;font-size:7.5px;line-height:1.75;color:var(--muted)}
.divider{left:416px;top:922px;width:1px;height:92px;background:#ddd}
.person{left:456px;top:905px;width:104px;height:133px;background:linear-gradient(180deg,#f1eeea 0%,#b8c4d2 100%)}
.contact-btn{left:609px;top:945px;width:114px;height:62px;font-size:11px;padding-top:14px}
/* footer */
.footer{left:0;top:1038px;width:834px;height:162px;background:var(--footer);color:#ddd}
.footer:after{content:"";position:absolute;left:0;bottom:0;width:834px;height:5px;background:var(--orange)}
.f-brand{left:92px;top:10px;display:flex;align-items:center;gap:7px}
.f-brand .brand-mark{width:26px;height:26px;background:var(--white)}
.f-brand .brand-name{color:var(--white);font-size:15px}
.f-about{left:92px;top:48px;width:135px;font-size:6.8px;line-height:1.7}
.f-social{left:96px;top:132px;display:flex;gap:14px}
.f-col h5{font-size:12px;font-weight:700;color:var(--white);padding-bottom:5px;border-bottom:1px solid #666;width:90px;position:relative}
.f-col h5:after{content:"";position:absolute;left:0;bottom:-1px;width:18px;height:2px;background:var(--orange)}
.f-col ul{list-style:none;font-size:7.5px;margin-top:10px}
.f-col li{margin-bottom:10px;padding-left:12px;position:relative}
.f-col li:before{content:"»";position:absolute;left:0}
.f-col li.on{color:var(--orange)}
.f-col .c{list-style:none}
.f-col .c li:before{content:"•"}
.f-col p{font-size:7.2px;line-height:1.45;margin-top:8px;width:135px}
.email{width:129px;height:20px;border:1px solid var(--orange);background:#2e2e2e;font-size:7px;color:#999;padding:5px;margin-top:10px}
.sub-btn{left:677px;top:119px;width:49px;height:17px;font-size:7px;line-height:17px}
</style>
</head>
<body>

<div class="abs topbar">
  <div class="abs contact"><span><i class="sq"></i>0200001234</span><span><i class="sq"></i>info@bastionsecurity.com</span></div>
  <div class="abs social"><i class="dot"></i><i class="dot"></i><i class="dot"></i><i class="dot"></i></div>
</div>

<header>
  <div class="abs brand"><span class="brand-mark"></span><span class="brand-name">Bastion</span></div>
  <nav class="abs nav"><span>Home</span><span>About Us</span><span>Products</span><span>Services</span><span>FAQS</span><span>Testimonials</span><span>Contact Us</span></nav>
</header>

<section class="abs hero">
  <svg class="abs arrow" style="left:34px" width="12" height="20" viewBox="0 0 12 20"><path d="M10 2 2 10l8 8" fill="none" stroke="var(--navy)" stroke-width="3"/></svg>
  <div class="abs slide">
    <div class="abs slide-art" role="img" aria-label="Security cameras with a recorder beside a phone showing live camera feeds"></div>
    <div class="abs caption">We Specialize in Consulting Supplying &amp; installing Electronic Security System</div>
  </div>
  <svg class="abs arrow" style="left:787px" width="12" height="20" viewBox="0 0 12 20"><path d="M2 2l8 8-8 8" fill="none" stroke="var(--navy)" stroke-width="3"/></svg>
</section>

<section>
  <div class="abs service" style="left:79px">
    <div class="icon"><svg width="52" height="52" viewBox="0 0 52 52"><rect x="14" y="18" width="22" height="10" rx="2" fill="#fff" transform="rotate(-20 25 23)"/><rect x="34" y="26" width="3" height="12" fill="#fff"/></svg></div>
    <h3>CCTV Camera</h3><p>Lorem Ipsum is simply dummy text of the printing and type-setting industry.</p>
  </div>
  <div class="abs service" style="left:193px">
    <div class="icon"><svg width="52" height="52" viewBox="0 0 52 52"><path d="M21 24v-5a5 5 0 0 1 10 0v5" fill="none" stroke="#fff" stroke-width="2.5"/><rect x="18" y="24" width="16" height="14" rx="3" fill="#fff"/><circle cx="26" cy="30" r="2" fill="var(--navy)"/></svg></div>
    <h3>Acess Control</h3><p>Lorem Ipsum is simply dummy text of the printing and type-setting industry.</p>
  </div>
  <div class="abs service" style="left:306px">
    <div class="icon"><svg width="52" height="52" viewBox="0 0 52 52"><path d="M19 34v-9a7 7 0 0 1 14 0v9z" fill="#fff"/><rect x="16" y="34" width="20" height="4" fill="#fff"/><path d="M26 10v4M14 16l3 3M38 16l-3 3M10 26h4M42 26h-4" stroke="#fff" stroke-width="2"/></svg></div>
    <h3>Alarms</h3><p>Lorem Ipsum is simply dummy text of the printing and type-setting industry.</p>
  </div>
  <div class="abs service" style="left:419px">
    <div class="icon"><svg width="52" height="52" viewBox="0 0 52 52"><circle cx="26" cy="26" r="11" fill="none" stroke="#fff" stroke-width="2.5"/><path d="M18 22c4 0 5 3 8 3s2 6 5 6M26 15c0 4 3 4 6 5" fill="none" stroke="#fff" stroke-width="2"/></svg></div>
    <h3>Intercome &amp;<br>Networking Cabelling</h3><p>Lorem Ipsum is simply dummy text of the printing and type-setting industry.</p>
  </div>
  <div class="abs about">
    <p>Lorem Ipsum is simply dummy text of the printing and typesetting industry. Lorem Ipsum has been the industry's standard dummy text ever since the 1500s, when an unknown printer took a galley of type and scrambled it to make a type specimen book.</p>
    <p>It has survived not only five centuries, but also the leap into electronic typesetting, remaining essentially unchanged.</p>
  </div>
</section>

<section class="abs band">
  <q>The traditional Supplier/Consumer relationship has been replaced with a partnership and we now have a resilient, reliable IT solution combined with fantastic customer service.</q>
  <div class="abs btn">Purchase Now</div>
</section>

<section class="abs pride">
  <div class="abs pride-photo" role="img" aria-label="Grey dome security camera with infrared lights"></div>
  <div class="abs pager"><span></span><span></span><span></span><span></span></div>
  <p class="abs intro">We pride our selves in giving our customers peace of mind giving back security and freedom to our customers. We pride in customer service quality products and expertise with and we do the job as though it is for our personal friends and family.</p>
  <div class="abs point" style="left:371px;top:73px">
    <svg width="20" height="20" viewBox="0 0 20 20"><circle cx="10" cy="10" r="8" fill="none" stroke="#999" stroke-width="1.5"/><circle cx="7" cy="8" r="1" fill="#999"/><circle cx="13" cy="8" r="1" fill="#999"/><path d="M6 12q4 4 8 0" fill="none" stroke="#999" stroke-width="1.5"/></svg>
    <h4>Peace of mind giving back</h4><p>Lorem Ipsum is simply dummy text of the printing and typesetting industry. Lorem Ipsum has been the industry's scrambled it to make a type specimen book.</p>
  </div>
  <div class="abs point" style="left:598px;top:73px">
    <svg width="20" height="20" viewBox="0 0 20 20"><circle cx="10" cy="10" r="5" fill="none" stroke="#999" stroke-width="4" stroke-dasharray="3 2"/></svg>
    <h4>Freedom To Our Customers</h4><p>Lorem Ipsum is simply dummy text of the printing and typesetting industry. Lorem Ipsum has been the industry's scrambled it to make a type specimen book.</p>
  </div>
  <div class="abs point" style="left:371px;top:163px">
    <svg width="20" height="20" viewBox="0 0 20 20"><rect x="2" y="9" width="4" height="9" fill="#999"/><path d="M7 9l4-7c2 0 2 2 1 5h5v10H7z" fill="#999"/></svg>
    <h4>Quality Products</h4><p>Lorem Ipsum is simply dummy text of the printing and typesetting industry. Lorem Ipsum has been the industry's scrambled it to make a type specimen book.</p>
  </div>
  <div class="abs point" style="left:598px;top:163px">
    <svg width="24" height="20" viewBox="0 0 24 20"><circle cx="6" cy="6" r="3" fill="#999"/><circle cx="18" cy="6" r="3" fill="#999"/><circle cx="12" cy="8" r="3.5" fill="#999"/><path d="M1 15a5 5 0 0 1 10 0zM13 15a5 5 0 0 1 10 0zM6 19a6 6 0 0 1 12 0z" fill="#999"/></svg>
    <h4>Give Service as our Personal</h4><p>Lorem Ipsum is simply dummy text of the printing and typesetting industry. Lorem Ipsum has been the industry's scrambled it to make a type specimen book.</p>
  </div>
</section>

<section class="ready">
  <h2 class="abs">Ready To Get Purchased ?</h2>
  <p class="abs">Lorem Ipsum is simply dummy text of the printing and typesetting industry. Lorem Ipsum has been the industry's standard dummy text ever since the 1500s, when an unknown printer took a galley of type and scrambled it to make a type specimen book.</p>
  <div class="abs divider"></div>
  <div class="abs person" role="img" aria-label="Smiling customer giving two thumbs up"></div>
  <div class="abs btn contact-btn">
    <svg width="20" height="14" viewBox="0 0 20 14" style="display:block;margin:0 auto 6px"><rect width="20" height="14" rx="1" fill="#fff"/><path d="M1 1l9 7 9-7" fill="none" stroke="var(--orange)" stroke-width="1.5"/></svg>
    Contact Us
  </div>
</section>

<footer class="abs footer">
  <div class="abs f-brand"><span class="brand-mark"></span><span class="brand-name">Bastion</span></div>
  <p class="abs f-about">Lorem Ipsum is simply dummy text of the printing and typesetting industry. Lorem Ipsum has been the industry's standard dummy text ever since the 1500s, when an unknown printer took a galley of type and scrambled it to make a type speci-</p>
  <div class="abs f-social"><i class="dot"></i><i class="dot"></i><i class="dot"></i><i class="dot"></i><i class="dot"></i></div>
  <div class="abs f-col" style="left:259px;top:27px">
    <h5>Contact</h5>
    <ul class="c"><li>Harbour Street Corporate<br>Headquarters</li><li>555.010.4821</li><li>info@bastionsecurity.com</li></ul>
  </div>
  <div class="abs f-col" style="left:432px;top:27px">
    <h5>Resources</h5>
    <ul><li class="on">Home</li><li>About Us</li><li>Services</li><li>Blog</li></ul>
  </div>
  <div class="abs f-col" style="left:599px;top:27px">
    <h5>Subscribe</h5>
    <p>Subscribe to our newsletter to receive news, updates, free stuff and new releases by email. We don't do spam.</p>
    <div class="email">Enter your email address</div>
  </div>
  <svg class="abs" style="left:604px;top:120px" width="22" height="15" viewBox="0 0 22 15"><rect x="1" y="1" width="20" height="13" fill="#eee" transform="rotate(-10 11 7)"/></svg>
  <div class="abs btn sub-btn">Subscribe</div>
</footer>

</body>
</html>
```